"Oral Surgery Office needs a Business Card Design with Logo"

We need a logo design and business card. The name of the office is Halvering Oral Surgery & Implant Center. The final design should communicate uniqueness as well as highly class office. The business card should emphasize power. I included the current business card below. Please design something unique

Target Market(s)

Dentists & Patients

Industry/Entity Type

Dental

Contact Information for Business Card

Unique Design to show success, prestige, Style, unmatched performance

Font styles to use
Serif

Colors
1b1b1b
ffffff
0556a4

Requirements
Must have
• Bussiness Name, Doctor's Name, Website, phone and Fax, email, office address
• Color should be either Black and White or Blue and White
Nice to have
• Clean look
Should not have
• the business card shouldn't be too busy. I feel like the old business card was too busy

```html
<!DOCTYPE html>
<html lang="en">
<head>
<meta charset="utf-8">
<title>Halvering Oral Surgery &amp; Implant Center — Business Card</title>
<link rel="stylesheet" href="https://fonts.googleapis.com/css2?family=Roboto+Condensed:wght@400;700&display=swap">
<style>
  :root {
    --navy: #134d7c;
    --white: #ffffff;
    --rule-grey: #555555;
    --page: #ecebe8;
    --shadow: rgba(0, 0, 0, 0.22);
  }
  * { margin: 0; padding: 0; box-sizing: border-box; }
  html, body {
    width: 991px;
    height: 1200px;
    overflow: hidden;
  }
  body {
    background: var(--page);
    position: relative;
    font-family: "Roboto Condensed", "Arial Narrow", sans-serif;
  }
  .card {
    position: absolute;
    background: var(--navy);
    box-shadow: 0 3px 10px var(--shadow);
    overflow: hidden;
  }
  .card--front { left: 149px; top: 126px; width: 705px; height: 408px; }
  .card--back  { left: 140px; top: 653px; width: 711px; height: 423px; }

  .front-curve {
    position: absolute;
    left: 0; top: 0;
    width: 705px; height: 408px;
  }

  .brand-mark {
    position: absolute;
    display: flex;
    align-items: center;
    justify-content: center;
    border-radius: 50%;
    text-align: center;
    text-transform: uppercase;
    font-weight: 400;
    line-height: 1.25;
  }
  .card--front .brand-mark {
    left: 40px; top: 110px;
    width: 180px; height: 180px;
    border: 3px solid var(--navy);
    color: var(--navy);
    font-size: 15px;
    letter-spacing: 1px;
  }
  .card--back .brand-mark {
    left: 245px; top: 100px;
    width: 222px; height: 222px;
    border: 3px solid var(--white);
    color: var(--white);
    font-size: 18px;
    letter-spacing: 1.5px;
  }

  .contact-block {
    position: absolute;
    right: 57px;
    top: 52px;
    text-align: right;
    color: var(--white);
  }
  .doctor-name {
    font-size: 22px;
    font-weight: 700;
    letter-spacing: 0.3px;
  }
  .doctor-title {
    font-size: 18px;
    font-weight: 400;
    margin-top: 2px;
  }
  .contact-list {
    list-style: none;
    margin-top: 28px;
  }
  .contact-list li {
    display: flex;
    align-items: center;
    justify-content: flex-end;
    font-size: 17px;
    height: 30px;
  }
  .contact-icon {
    width: 18px; height: 18px;
    margin-left: 8px;
    flex: none;
  }
</style>
</head>
<body>

<section class="card card--front" aria-label="Business card front">
  <svg class="front-curve" viewBox="0 0 705 408" aria-hidden="true">
    <path d="M0 0 H110 C 340 55 340 353 110 408 H0 Z" fill="#ffffff"/>
    <path d="M118 0 C 352 55 352 353 118 408" fill="none" stroke="#555555" stroke-width="3"/>
  </svg>

  <div class="brand-mark">Halvering<br>Oral Surgery &amp;<br>Implant Center</div>

  <div class="contact-block">
    <h1 class="doctor-name">DR. Marten Vello, D.D.S.</h1>
    <p class="doctor-title">Oral and Maxillofacial Surgery</p>
    <ul class="contact-list">
      <li>4820 Larkmoor Avenue, Halvering, NY 10990
        <svg class="contact-icon" viewBox="0 0 18 18" aria-hidden="true"><path d="M1 8 L9 2 L17 8 V16 H1 Z" fill="#fff"/><rect x="5" y="10" width="8" height="2" fill="#134d7c"/></svg>
      </li>
      <li>555-014-4700
        <svg class="contact-icon" viewBox="0 0 18 18" aria-hidden="true"><path d="M4 1 L7 5 L5 7 C6 10 8 12 11 13 L13 11 L17 14 L15 17 C8 17 1 10 1 3 Z" fill="#fff"/></svg>
      </li>
      <li>555-014-5006
        <svg class="contact-icon" viewBox="0 0 18 18" aria-hidden="true"><rect x="4" y="1" width="10" height="5" fill="#fff"/><rect x="1" y="7" width="16" height="7" rx="1" fill="#fff"/><rect x="4" y="12" width="10" height="5" fill="#fff" stroke="#134d7c"/></svg>
      </li>
      <li>HalveringOralSurgeryCenter.com
        <svg class="contact-icon" viewBox="0 0 18 18" aria-hidden="true"><rect x="1.5" y="4" width="15" height="10" fill="none" stroke="#fff" stroke-width="1.5"/><path d="M1.5 4 L9 10 L16.5 4" fill="none" stroke="#fff" stroke-width="1.5"/></svg>
      </li>
      <li>www.HalveringOralSurgeryCenter.com
        <svg class="contact-icon" viewBox="0 0 18 18" aria-hidden="true"><g fill="none" stroke="#fff" stroke-width="1.4"><circle cx="9" cy="9" r="7.5"/><ellipse cx="9" cy="9" rx="3.5" ry="7.5"/><path d="M1.5 9 H16.5 M3 5 H15 M3 13 H15"/></g></svg>
      </li>
    </ul>
  </div>
</section>

<section class="card card--back" aria-label="Business card back">
  <div class="brand-mark">Halvering<br>Oral Surgery &amp;<br>Implant Center</div>
</section>

</body>
</html>
```